A Gallery type Web design

We are developing a Wordpress based website for a client that does design construction projects. E.g. Pools, Lobbies, Toilets, etc. The website will mainly be to showcase their past projects and the collections they have.
No programming required, we just need the designs!
A sample of what the client is looking for:
http://velmora.it/
Pages to include:
• Home – A nice slider design to showcase selected photos
• Main Category Template
• Sub Category Template
• About us
• Contact us
Example of their Main Categories and their Sub Categories:
Collections - Granite
- Marble
- Sculpture
Projects - Private
- Public
- Commercial
- Overseas
Installation - Vanity tops
- Hall areas
- Toilets
The Main Category is to show a sample and link the user to the respective Sub Categories. The Sub Categories are to showcase all the photos they have from the category. Please leave a little space to add some text or caption for the photo.
Designs need to be mobile responsive!
I've attached their logo and some sample photos to use for mock ups. Let me know if you have any questions!

```html
<!DOCTYPE html>
<html lang="en">
<head>
<meta charset="utf-8">
<title>Petra Hall – Home</title>
<link href="https://fonts.googleapis.com/css2?family=Arimo:wght@400;700&display=swap" rel="stylesheet">
<style>
:root{
  --red:#c4161c;
  --ink:#333333;
  --muted:#8a8a8a;
  --text:#666666;
  --strip:#f2f2f2;
  --footer:#444446;
  --white:#ffffff;
}
*{margin:0;padding:0;box-sizing:border-box}
html,body{width:1046px;height:1200px;overflow:hidden}
body{font-family:"Arimo",Arial,sans-serif;background:var(--white);color:var(--ink);position:relative}
.topline{position:absolute;left:0;top:0;width:1046px;height:3px;background:var(--red);z-index:5}
.hero{position:absolute;left:0;top:0;width:1046px;height:584px;
  background:
    linear-gradient(180deg,rgba(0,0,0,0) 0%,rgba(0,0,0,0) 55%,rgba(150,150,146,.55) 78%,rgba(190,190,186,.85) 100%),
    radial-gradient(ellipse at 70% 30%,#d9cfbf 0%,#8d8576 35%,#3f3b36 70%,#1f1d1b 100%)}
.header{position:absolute;left:86px;top:3px;width:874px;height:78px;background:rgba(255,255,255,.94);box-shadow:0 2px 4px rgba(0,0,0,.25);z-index:4}
.brand{position:absolute;left:14px;top:22px;display:flex;align-items:center;gap:8px}
.brand-mark{width:26px;height:26px;background:var(--red)}
.brand-name{font-weight:700;font-size:20px;color:var(--red)}
.nav{position:absolute;top:34px;left:0;font-size:11.5px;color:#777}
.nav a{position:absolute;white-space:nowrap;color:#777;text-decoration:none}
.nav a.active{color:var(--red)}
.dropdown{position:absolute;left:449px;top:61px;width:134px;z-index:6}
.dropdown::before{content:"";position:absolute;left:6px;top:-6px;border:6px solid transparent;border-top:0;border-bottom-color:var(--red)}
.dropdown a{display:block;height:29px;line-height:29px;padding-left:13px;background:var(--red);color:var(--white);font-weight:700;font-size:11.5px;text-decoration:none;border-bottom:1px solid rgba(255,255,255,.5)}
.hero-copy{position:absolute;left:0;top:288px;width:1046px;text-align:center;z-index:3;text-shadow:0 2px 4px rgba(0,0,0,.5)}
.hero-welcome{font-weight:700;font-size:38px;color:var(--white);line-height:44px}
.hero-title{display:flex;justify-content:center;align-items:center;gap:12px;font-weight:700;font-size:58px;color:var(--red);line-height:60px;margin-top:4px}
.hero-title .rule{width:64px;height:4px;border-top:1px solid #fff;border-bottom:1px solid #fff}
.hero-tag{font-weight:700;font-size:15.5px;color:var(--white);margin-top:14px}
.hero-arrows{position:absolute;left:477px;top:454px;z-index:3}
.strip{position:absolute;left:0;top:584px;width:1046px;height:95px;background:var(--strip);border-bottom:1px solid #e4e4e4}
.cat{position:absolute;top:13px;display:flex;gap:20px}
.cat-thumb{width:73px;height:69px;border:1px solid #ddd}
.cat h3{font-size:13px;color:var(--red);font-weight:400;margin-top:1px;letter-spacing:.2px}
.cat p{font-size:8.8px;line-height:16.5px;color:#aaa;width:180px;margin-top:4px}
.latest{position:absolute;left:0;top:704px;width:1046px;text-align:center}
.latest h2{font-size:19px;font-weight:700;color:var(--ink)}
.latest h2 span{color:var(--red)}
.latest p{font-size:9px;line-height:17px;color:var(--text);width:640px;margin:12px auto 0}
.card{position:absolute;top:798px;width:202px}
.card-photo{width:202px;height:144px;border:2px solid #e6e6e6}
.card p{font-size:9px;line-height:17px;color:var(--muted);margin-top:15px}
.card p a{color:var(--red);text-decoration:none}
.footer{position:absolute;left:0;top:1042px;width:1046px;height:158px;background:var(--footer);color:var(--white)}
.social{position:absolute;left:396px;top:26px;display:flex;gap:7.6px}
.social a{width:30px;height:30px;border-radius:50%;background:var(--white);display:flex;align-items:center;justify-content:center}
.social a::after{content:"";width:12px;height:12px;border-radius:50%;border:2.5px solid var(--footer)}
.footer-rule{position:absolute;left:86px;top:73px;width:874px;height:1px;background:#5a5a5c}
.footer-nav{position:absolute;left:0;top:87px;width:1046px;text-align:center;font-size:9px;word-spacing:1px}
.footer-nav a{color:var(--white);text-decoration:none}
.footer-nav i{font-style:normal;margin:0 14px}
.copy{position:absolute;left:0;top:118px;width:1046px;text-align:center;font-size:8.8px}
</style>
</head>
<body>
<div class="topline"></div>

<section class="hero" role="img" aria-label="Elegant foyer interior with dining chairs, a console table with lamp and frames, and a black-and-white mosaic floor"></section>

<header class="header">
  <div class="brand"><span class="brand-mark"></span><span class="brand-name">Petra Hall</span></div>
  <nav class="nav">
    <a style="left:292px">HOME</a>
    <a class="active" style="left:364px">COLLECTIONS</a>
    <a style="left:480px">PROJECTS</a>
    <a style="left:576px">INSTALLATIONS</a>
    <a style="left:698px">ABOUT US</a>
    <a style="left:792px">CONTACT US</a>
  </nav>
</header>
<div class="dropdown">
  <a>GRANITE</a><a>MARBLE</a><a>SCULPTURE</a>
</div>

<div class="hero-copy">
  <div class="hero-welcome">WELCOME</div>
  <div class="hero-title"><span class="rule"></span>PETRA HALL<span class="rule"></span></div>
  <div class="hero-tag">IT IS A LONG ESTABLISHED FACT THAT A WHEN LOOKING AT ITS LAYOUT</div>
</div>
<svg class="hero-arrows" width="92" height="42" viewBox="0 0 92 42">
  <circle cx="20" cy="20" r="19" fill="none" stroke="#fff" stroke-width="2"/>
  <path d="M23 12 L15 20 L23 28" fill="none" stroke="#fff" stroke-width="3" stroke-linecap="round"/>
  <circle cx="73" cy="20" r="19" fill="none" stroke="#fff" stroke-width="2"/>
  <path d="M70 12 L78 20 L70 28" fill="none" stroke="#fff" stroke-width="3" stroke-linecap="round"/>
</svg>

<section class="strip">
  <div class="cat" style="left:94px">
    <div class="cat-thumb" role="img" aria-label="Granite mosaic tiles" style="background:linear-gradient(135deg,#6b5848,#c9b79f,#3b2e25)"></div>
    <div><h3>GRANITE</h3><p>It is a long established fact that a reader will be distracted by the readable content of a page when looking at its layout.</p></div>
  </div>
  <div class="cat" style="left:390px">
    <div class="cat-thumb" role="img" aria-label="White marble tiles" style="background:linear-gradient(135deg,#f2f2f2,#cfcfcf,#e8e8e8)"></div>
    <div><h3>MARBLE</h3><p>It is a long established fact that a reader will be distracted by the readable content of a page when looking at its layout.</p></div>
  </div>
  <div class="cat" style="left:682px">
    <div class="cat-thumb" role="img" aria-label="Dark sculpted stone tile" style="background:linear-gradient(135deg,#1c1a17,#8a7b62,#1c1a17)"></div>
    <div><h3>SCULPTURE</h3><p>It is a long established fact that a reader will be distracted by the readable content of a page when looking at its layout.</p></div>
  </div>
</section>

<section class="latest">
  <h2>LATEST <span>COLLECTIONS</span></h2>
  <p>Sed ut perspiciatis unde omnis iste natus error sit voluptatem accusantium doloremque laudantium, totam rem aperiam, eaque ipsa quae ab illo inventore veritatis et quasi architecto beatae vitae dicta sunt explicabo.</p>
</section>

<article class="card" style="left:86px">
  <div class="card-photo" role="img" aria-label="Bathroom with dark mosaic wall and white basins" style="background:linear-gradient(90deg,#5d6670,#9aa3ab 40%,#2f363d)"></div>
  <p>It is a long established fact that a reader will be distracted by the readable content of a page when of letters, as opposed....<a>VIEW MORE</a></p>
</article>
<article class="card" style="left:311px">
  <div class="card-photo" role="img" aria-label="Fireplace set in a dark mosaic wall with firewood" style="background:linear-gradient(180deg,#3a3532,#6e5a48 60%,#d8d0c4)"></div>
  <p>It is a long established fact that a reader will be distracted by the readable content of a page when of letters, as opposed....<a>VIEW MORE</a></p>
</article>
<article class="card" style="left:535px">
  <div class="card-photo" role="img" aria-label="Room with silver mosaic wall and a wooden chair" style="background:linear-gradient(135deg,#d9d9d6,#9e9b95 60%,#6d6a66)"></div>
  <p>It is a long established fact that a reader will be distracted by the readable content of a page when of letters, as opposed....<a>VIEW MORE</a></p>
</article>
<article class="card" style="left:757px">
  <div class="card-photo" role="img" aria-label="Chandelier in front of gold and grey mosaic wall" style="background:linear-gradient(135deg,#c9a548,#8f8a80 50%,#d4b25a)"></div>
  <p>It is a long established fact that a reader will be distracted by the readable content of a page when of letters, as opposed....<a>VIEW MORE</a></p>
</article>

<footer class="footer">
  <div class="social"><a aria-label="Social link 1"></a><a aria-label="Social link 2"></a><a aria-label="Social link 3"></a><a aria-label="Social link 4"></a><a aria-label="Social link 5"></a><a aria-label="Social link 6"></a><a aria-label="Social link 7"></a></div>
  <div class="footer-rule"></div>
  <nav class="footer-nav"><a>HOME</a><i>/</i><a>COLLECTIONS</a><i>/</i><a>PROJECTS</a><i>/</i><a>INSTALLATIONS</a><i>/</i><a>ABOUT US</a><i>/</i><a>CONTACT US</a></nav>
  <div class="copy">© Copy Rights 2014 Petra Hall.All Rights Reserved</div>
</footer>
</body>
</html>
```